QT Bridgeway Business Card design

I need a business card design based on the logo you did for me.

Some where it should say "Online & Social Media Marketing"

I would like to see how you would do a double sided design. Although I may go with one side and have the other side just a sold color.

Industry/Entity Type

Business

```html
<!DOCTYPE html>
<html lang="en">
<head>
<meta charset="utf-8">
<title>QT Bridgeway Business Card</title>
<link rel="stylesheet" href="https://fonts.googleapis.com/css2?family=Baskervville&display=swap">
<style>
  :root {
    --page: #dddddd;
    --card: #ffffff;
    --ink: #111111;
    --olive: #948a54;
    --olive-dark: #8a7f4c;
    --rule: #000000;
    --white: #ffffff;
    --icon: #e4e4e4;
    --icon-edge: #c8c8c8;
  }
  * { margin: 0; padding: 0; box-sizing: border-box; }
  html, body {
    width: 1200px; height: 1000px; overflow: hidden;
    background: var(--page);
    font-family: "Baskervville", "Libre Baskerville", Georgia, serif;
    color: var(--ink);
  }
  .card {
    position: absolute; left: 58px; top: 182px;
    width: 1085px; height: 634px;
    background: var(--card);
  }
  .brand {
    position: absolute; left: 30px; top: 42px;
    display: flex; align-items: center; gap: 14px;
  }
  .brand-name {
    font-size: 48px; color: var(--olive-dark); line-height: 1;
  }
  .brand-dot {
    width: 22px; height: 22px; border-radius: 50%;
    background: var(--olive-dark);
  }
  .social {
    position: absolute; left: 804px; top: 22px;
    list-style: none;
  }
  .social li {
    display: flex; align-items: center; height: 55px;
    font-size: 20px;
  }
  .social-icon {
    width: 38px; height: 38px; border-radius: 50%;
    background: var(--icon); border: 2px solid var(--icon-edge);
    margin-right: 26px;
  }
  .identity {
    position: absolute; left: 0; right: 0; top: 236px;
    text-align: center;
  }
  .person-name { font-size: 44px; font-weight: 400; letter-spacing: 1px; line-height: 1.1; }
  .person-role { font-size: 23px; margin-top: 8px; }
  .website {
    position: absolute; left: 0; right: 0; top: 434px;
    text-align: center; font-size: 27px;
  }
  .footer {
    position: absolute; left: 0; bottom: 0;
    width: 100%; height: 153px;
    background: var(--olive);
    border-top: 5px solid var(--rule);
  }
  .contact {
    position: absolute; left: 47px; top: 22px;
    list-style: none; font-size: 25px; color: var(--ink);
  }
  .contact li { height: 50px; display: flex; align-items: center; }
  .contact-label { color: var(--white); width: 34px; }
  .address {
    position: absolute; left: 722px; top: 24px;
    font-size: 28px; line-height: 50px; font-style: normal;
  }
</style>
</head>
<body>
  <div class="card">
    <div class="brand">
      <span class="brand-name">QT Bridgeway</span>
      <span class="brand-dot"></span>
    </div>

    <ul class="social">
      <li><span class="social-icon"></span>qtbridgeway</li>
      <li><span class="social-icon"></span>qtbridgewaycolby</li>
      <li><span class="social-icon"></span>@QTBRIDGEWAY</li>
      <li><span class="social-icon"></span>QT Bridgeway</li>
    </ul>

    <div class="identity">
      <h1 class="person-name">MAREN COLBY</h1>
      <p class="person-role">Online &amp; Social Media Marketing</p>
    </div>

    <p class="website">www.QTBRIDGEWAY.com</p>

    <div class="footer">
      <ul class="contact">
        <li><span class="contact-label">p</span>555.214.0386</li>
        <li><span class="contact-label">e</span>maren@qtbridgeway.com</li>
      </ul>
      <address class="address">24 Alder Lane<br>Harborview, MA 01990</address>
    </div>
  </div>
</body>
</html>
```